VantoMedix website

I have a plumfield hosting website already & have been using wordpress.
See www.vantomedix-sample.com
I have a logo's already.
I need a front page "VantoMedix". I have 3 products: (need separate pages)
1) the "GlideTray" (can't supply images ATM)
2) the "TubeKeeper" (several stills below & animation: http://www.clipvault-example.com/watch?v=Z7HqR20mW3x&list=QPtr8B_kzoepWnXcM4Lq5B_T&feature=share)
3) the "FastPart" animation here: http://clipv.example/pwrtk-Mmo_E & logo as below

It needs to be corporate & professional looking. VantoMedix is an innovative design house for medical devices.

Reason: Hi Designers, thanks for all your work to date - there have been some great designs. We'll be providing feedback to some of you in the near future. The reason we have extended the deadline is simply that we are too busy with other aspects of the business to focus on this at the moment. Kind regards, the VantoMedix team.

Dear Designers,

VantoMedix apologies for the delay due to our busyness. 
Please help us to understand the process here:
are we getting fully working websites? With multiple pages? Will we be able to modify them?
If not, what is the output?

Kind regards,
the Vanto team.

```html
<!DOCTYPE html>
<html lang="en">
<head>
<meta charset="utf-8">
<title>VantoMedix</title>
<link rel="stylesheet" href="https://fonts.googleapis.com/css2?family=Open+Sans:wght@300;400;600;700&display=swap">
<style>
  :root {
    --orange: #f26a1b;
    --sky: #36b1e6;
    --sky-deep: #2a9fd6;
    --footer-blue: #35b0e3;
    --ink: #333333;
    --muted: #8c8c8c;
    --soft: #9a9a9a;
    --band: #f2f2f2;
    --white: #ffffff;
    --rule: #e3e3e3;
  }
  * { box-sizing: border-box; margin: 0; padding: 0; }
  html, body { width: 781px; height: 1200px; overflow: hidden; background: var(--white); }
  body { font-family: "Open Sans", Arial, sans-serif; color: var(--ink); }
  .page { position: relative; width: 781px; height: 1200px; overflow: hidden; }
  .abs { position: absolute; }

  /* header */
  .site-header { position: absolute; left: 0; top: 0; width: 781px; height: 62px; background: var(--white); }
  .brand { position: absolute; left: 78px; top: 13px; font-size: 28px; font-weight: 700; color: var(--orange); letter-spacing: -0.5px; line-height: 34px; }
  .main-nav a { position: absolute; top: 35px; font-size: 11px; color: #777; text-decoration: none; line-height: 14px; }
  .main-nav a.active { color: var(--orange); }
  .nav-underline { position: absolute; left: 366px; top: 59px; width: 52px; height: 3px; background: var(--orange); }

  /* hero */
  .hero { position: absolute; left: 0; top: 62px; width: 781px; height: 275px;
    background: linear-gradient(100deg, #3aa8dc 0%, #44b6e8 40%, #3cb3e6 70%, #57c0ec 100%); }
  .hero-title { position: absolute; left: 0; width: 781px; top: 38px; text-align: center; font-size: 35px; font-weight: 400; color: var(--white); line-height: 44px; }
  .hero-sub { position: absolute; left: 0; width: 781px; top: 88px; text-align: center; font-size: 20px; font-weight: 400; color: var(--white); line-height: 24px; }
  .play-button { position: absolute; left: 355px; top: 154px; width: 68px; height: 68px; }
  .hero-cta { position: absolute; left: 0; width: 781px; top: 230px; text-align: center; font-size: 11.5px; font-weight: 700; color: var(--white); letter-spacing: 0.6px; }

  /* facts */
  .injury-chart { position: absolute; left: 69px; top: 360px; width: 291px; height: 169px; }
  .facts-title { position: absolute; left: 436px; top: 358px; font-size: 26px; font-weight: 300; color: var(--orange); line-height: 34px; }
  .facts-text { position: absolute; left: 374px; top: 407px; font-size: 10.8px; font-weight: 300; color: var(--soft); line-height: 16.4px; }
  .facts-text span { display: block; white-space: nowrap; }

  /* products */
  .section-title { position: absolute; left: 0; width: 781px; text-align: center; font-weight: 400; color: var(--orange); }
  .products-title { top: 575px; font-size: 28px; line-height: 36px; }
  .products-intro { position: absolute; left: 70px; width: 641px; top: 622px; text-align: center; font-size: 10.8px; color: var(--muted); line-height: 16.5px; }
  .product-card { position: absolute; top: 683px; width: 199px; }
  .product-photo { width: 199px; height: 113px; }
  .photo-glidetray { background: linear-gradient(120deg, #d8d4cc 0%, #3f63b5 45%, #e0b84a 70%, #3a4c7a 100%); }
  .photo-tubekeeper { background: linear-gradient(135deg, #1c1c22 0%, #4b4a5a 35%, #a9a2d9 60%, #2b2b33 100%); }
  .photo-fastpart { background: linear-gradient(160deg, #c9b7a8 0%, #8a3b3e 40%, #6c2d33 70%, #d7c9bb 100%); }
  .product-name { margin-top: 20px; text-align: center; font-size: 17px; font-weight: 400; color: var(--ink); line-height: 22px; }
  .product-desc { margin-top: 2px; text-align: center; font-size: 9.6px; color: var(--muted); line-height: 14.5px; }
  .read-more { display: block; margin: 9px auto 0; width: 87px; height: 24px; background: var(--orange); color: var(--white); font-size: 10.8px; text-align: center; line-height: 24px; text-decoration: none; }

  /* testimonials */
  .testimonials { position: absolute; left: 0; top: 951px; width: 781px; height: 171px; background: var(--band); }
  .testimonials-title { top: 16px; font-size: 24px; line-height: 32px; }
  .quote { position: absolute; left: 118px; width: 545px; top: 55px; text-align: center; font-size: 10.8px; color: var(--muted); line-height: 16.5px; }
  .quote-name { position: absolute; left: 0; width: 781px; top: 121px; text-align: center; font-size: 10.5px; font-weight: 600; color: #666; }
  .quote-role { position: absolute; left: 0; width: 781px; top: 137px; text-align: center; font-size: 10.5px; color: var(--muted); }
  .slider-arrow { position: absolute; top: 53px; width: 26px; height: 48px; }

  /* footer */
  .site-footer { position: absolute; left: 0; top: 1122px; width: 781px; height: 78px; background: var(--footer-blue); color: var(--white); }
  .footer-brand { position: absolute; left: 78px; top: 12px; font-size: 21px; font-weight: 700; line-height: 26px; }
  .copyright { position: absolute; left: 78px; top: 45px; font-size: 8px; }
  .footer-heading { position: absolute; top: 15px; font-size: 8.7px; font-weight: 700; letter-spacing: 0.3px; }
  .footer-link { position: absolute; font-size: 8px; line-height: 12px; color: var(--white); text-decoration: none; }
  .social-dot { position: absolute; top: 32px; width: 17px; height: 17px; border-radius: 50%; background: var(--white); opacity: 0.95; }
</style>
</head>
<body>
<div class="page">

  <header class="site-header">
    <div class="brand">VantoMedix</div>
    <nav class="main-nav">
      <a class="active" href="#" style="left:378px">Home</a>
      <a href="#" style="left:447px">About</a>
      <a href="#" style="left:516px">FAQ</a>
      <a href="#" style="left:575px">Video</a>
      <a href="#" style="left:642px">Contact Us</a>
    </nav>
    <div class="nav-underline"></div>
  </header>

  <section class="hero" role="img" aria-label="Paramedics attending to a patient beside an ambulance, tinted blue">
    <h1 class="hero-title">VantoMedix</h1>
    <p class="hero-sub">has created a fully integrated system to help paramedics<br>remove patients from everyday awkward situations</p>
    <svg class="play-button" viewBox="0 0 68 68" aria-hidden="true">
      <circle cx="34" cy="34" r="34" fill="var(--orange)"/>
      <polygon points="26,19 26,49 50,34" fill="var(--white)"/>
    </svg>
    <div class="hero-cta">WATCH THE DEMO VIDEO</div>
  </section>

  <svg class="injury-chart" viewBox="80 415 335 195" aria-label="Occupational injury rates per 100 full-time workers per year">
    <g stroke="var(--rule)" stroke-width="1">
      <line x1="102" y1="425" x2="410" y2="425"/>
      <line x1="102" y1="444" x2="410" y2="444"/>
      <line x1="102" y1="463" x2="410" y2="463"/>
      <line x1="102" y1="482" x2="410" y2="482"/>
      <line x1="102" y1="501" x2="410" y2="501"/>
      <line x1="102" y1="519" x2="410" y2="519"/>
      <line x1="102" y1="538" x2="410" y2="538"/>
      <line x1="102" y1="557" x2="410" y2="557"/>
      <line x1="102" y1="576" x2="410" y2="576" stroke="#bbb"/>
    </g>
    <g font-family="Open Sans, Arial, sans-serif" font-size="8" fill="#555" text-anchor="end">
      <text x="96" y="428">40</text><text x="96" y="447">35</text><text x="96" y="466">30</text>
      <text x="96" y="485">25</text><text x="96" y="504">20</text><text x="96" y="522">15</text>
      <text x="96" y="541">10</text><text x="96" y="560">5</text><text x="96" y="579">0</text>
    </g>
    <text x="147" y="441" font-family="Open Sans, Arial, sans-serif" font-size="8" font-weight="700" fill="#111">Occupational Injury Rates per 100 FT workers per year</text>
    <rect x="130" y="455" width="77" height="86" fill="#3f79a8" role="img" aria-label="Illustration of a human back and spine"/>
    <rect x="125" y="555" width="20" height="21" fill="#5b9bd5"/>
    <rect x="187" y="550" width="19" height="26" fill="#5b9bd5"/>
    <rect x="248" y="524" width="19" height="52" fill="#5b9bd5"/>
    <rect x="308" y="507" width="19" height="69" fill="#5b9bd5"/>
    <rect x="368" y="445" width="21" height="131" fill="var(--orange)"/>
    <g font-family="Open Sans, Arial, sans-serif" font-size="8" fill="#555" text-anchor="middle">
      <text x="135" y="592">National</text><text x="135" y="603">average</text>
      <text x="196" y="592">Health workers</text>
      <text x="257" y="592">Police</text>
      <text x="318" y="592">Fire</text>
      <text x="378" y="592">EMS</text>
    </g>
  </svg>

  <h2 class="facts-title">Did you know?</h2>
  <p class="facts-text">
    <span>The cost of paramedic (EMS) injury in Australia is over $32,000 dollars</span>
    <span>a day?</span>
    <span>(That translates to well over half a billion dollars every year globally.)</span>
    <span>17% of injured paramedics remain off duty for over a month?</span>
    <span>Two thirds of injuries to paramedics affect the back and come from</span>
    <span>lifting &amp; carrying?</span>
  </p>

  <h2 class="section-title products-title">Introducing VantoMedix Products</h2>
  <p class="products-intro">Sed ut perspiciatis unde omnis iste natus error sit voluptatem accusantium doloremque laudantium, totam rem aperiam, eaque ipsa quae ab illo inventore veritatis et quasi architecto beatae vitae dicta sunt explicabo emo enim ipsam voluptatem.</p>

  <article class="product-card" style="left:78px">
    <div class="product-photo photo-glidetray" role="img" aria-label="Paramedics strapping a patient onto a rescue board"></div>
    <h3 class="product-name">GlideTray</h3>
    <p class="product-desc">Lorem ipsum dolor sit amet, consectetur<br>et dolore magna aliqua.</p>
    <a class="read-more" href="#">Read More</a>
  </article>
  <article class="product-card" style="left:291px">
    <div class="product-photo photo-tubekeeper" role="img" aria-label="Rendering of a line holder clipped onto a stretcher rail"></div>
    <h3 class="product-name">TubeKeeper</h3>
    <p class="product-desc">Lorem ipsum dolor sit amet, consectetur<br>et dolore magna aliqua.</p>
    <a class="read-more" href="#">Read More</a>
  </article>
  <article class="product-card" style="left:503px">
    <div class="product-photo photo-fastpart" role="img" aria-label="Rendering of a seated driver fitted with a coloured split harness"></div>
    <h3 class="product-name">FastPart</h3>
    <p class="product-desc">Lorem ipsum dolor sit amet, consectetur<br>et dolore magna aliqua.</p>
    <a class="read-more" href="#">Read More</a>
  </article>

  <section class="testimonials">
    <h2 class="section-title testimonials-title">Testimonials</h2>
    <svg class="slider-arrow" style="left:64px" viewBox="0 0 26 48" aria-hidden="true">
      <polyline points="24,1 2,24 24,47" fill="none" stroke="#d4d4d4" stroke-width="1.5"/>
    </svg>
    <p class="quote">Sed ut perspiciatis unde omnis iste natus error sit voluptatem accusantium doloremque laudantium, totam rem aperiam, eaque ipsa quae ab illo inventore veritatis et quasi architecto beatae vitae dicta sunt explicabo emo enim ipsam voluptatem anya makunam lakay mayat aya.</p>
    <div class="quote-name">John Doe Smith</div>
    <div class="quote-role">Paramedic, NY</div>
    <svg class="slider-arrow" style="left:676px" viewBox="0 0 26 48" aria-hidden="true">
      <polyline points="2,1 24,24 2,47" fill="none" stroke="#d4d4d4" stroke-width="1.5"/>
    </svg>
  </section>

  <footer class="site-footer">
    <div class="footer-brand">VantoMedix</div>
    <div class="copyright">Copyright © 2014 All Rights Reserved</div>

    <div class="footer-heading" style="left:269px">PAGES</div>
    <a class="footer-link" href="#" style="left:269px;top:28px">Home</a>
    <a class="footer-link" href="#" style="left:269px;top:40px">About</a>
    <a class="footer-link" href="#" style="left:311px;top:28px">Term &amp; Conditions</a>
    <a class="footer-link" href="#" style="left:311px;top:40px">Customer Service</a>
    <a class="footer-link" href="#" style="left:404px;top:28px">Legal</a>
    <a class="footer-link" href="#" style="left:404px;top:40px">FAQ</a>

    <div class="footer-heading" style="left:469px">CONTACT US</div>
    <div class="footer-link" style="left:469px;top:28px">phone: 05 987 65432</div>
    <div class="footer-link" style="left:469px;top:40px">email : info@vantomedix-sample.com</div>

    <div class="footer-heading" style="left:619px">CONNECT WITH US</div>
    <span class="social-dot" style="left:629px" aria-label="Social link"></span>
    <span class="social-dot" style="left:653px" aria-label="Social link"></span>
    <span class="social-dot" style="left:679px" aria-label="Social link"></span>
  </footer>

</div>
</body>
</html>
```